QuoteMarlin.com Homepage Redesign

Create a new homepage design for our website QuoteMarlin.com. Our current experience is focused on auto insurance only. We would like to incorporate the ability to receive rate estimates for home insurance and bundled (home + auto) insurance in addition to auto. Home insurance will include home, renters and condo. The final design should inspire users to utilize our comparison tool.

Industry/Entity Type

Insurance (Auto & Home)

Number of Pages Required

1 page

Font styles to use
Other font styles liked:
• See Assets - Sans Serif & Roboto

Colors
0054AA
0677BA
7BADD7
CADEEF
E8F1F8
59FF00
82FF00
B8FF75
E3FFCB
F4FFEA

Requirements
Must have
• Must include the ability to launch our rate comparison tool within the main hero image for Auto, Home, Bundled.
Nice to have
• The design should be bold and eye catching. It should be differentiated from the typical landing page experience. (Some of our favorite sites from a UX perspective include: Vaultline.org, ThePelican.com, Ferrow.com and Corvane Airways - They are busy but we like the app like approach on the homepage)
Should not have
• We are not looking for a design that is heavy on generic images.

```html
<!DOCTYPE html>
<html lang="en">
<head>
<meta charset="utf-8">
<title>QuoteMarlin — Compare insurance rates</title>
<link rel="stylesheet" href="https://fonts.googleapis.com/css2?family=Work+Sans:wght@500;600;700&family=Roboto:wght@400;500;700&display=swap">
<style>
:root{
  --navy:#0B2B5F;
  --blue:#0054AA;
  --accent:#1C6BEA;
  --sky:#7BADD7;
  --ice:#CADEEF;
  --pale:#E8F1F8;
  --soft:#EEF4FB;
  --green:#59FF00;
  --lime:#82FF00;
  --ink:#0F1A33;
  --muted:#4C5872;
  --line:#DDE5EE;
  --check:#3DBF4A;
  --white:#ffffff;
}
*{box-sizing:border-box;margin:0;padding:0}
html,body{width:1200px;height:4129px;overflow:hidden}
body{background:#fff;font-family:Roboto,Arial,sans-serif;color:var(--ink);position:relative}
.device{position:absolute;overflow:hidden;background:#fff;box-shadow:0 0 0 1px #e3e7ee,0 4px 18px rgba(10,30,70,.08)}
.desktop{left:26px;top:32px;width:894px;height:3197px}
.mobile{left:944px;top:32px;width:232px;height:4067px}
.abs{position:absolute}
.band{position:absolute;left:0;right:0}
.navy{background:var(--navy)}
.soft{background:var(--soft)}
.white{background:#fff}
h1,h2,h3{font-family:"Work Sans",Arial,sans-serif;font-weight:700;letter-spacing:.2px}
.hl{color:var(--accent)}
.hl-green{color:var(--green)}
.brand{display:flex;align-items:center;gap:6px;font-family:"Work Sans",Arial,sans-serif;font-weight:700;color:var(--navy)}
.brand-mark{background:var(--blue);border-radius:3px}
.nav{display:flex;gap:26px;font-size:9.5px;color:var(--ink)}
.btn{display:flex;align-items:center;justify-content:center;font-size:9.5px;font-weight:500;border-radius:3px}
.btn-solid{background:var(--accent);color:#fff}
.btn-dash{border:1.5px dashed var(--lime);color:var(--lime);background:transparent}
.photo{background:radial-gradient(ellipse at 55% 40%,#E6B25A 0%,#C98C34 45%,rgba(201,140,52,0) 75%)}
.type-card{position:absolute;background:#fff;border:2px dashed var(--lime);border-radius:6px;display:flex;flex-direction:column;align-items:center;justify-content:center;text-align:center;color:var(--navy);font-weight:700;line-height:1.15}
.type-card svg{stroke:var(--navy);fill:none;stroke-width:1.6;stroke-linejoin:round;stroke-linecap:round}
.type-card small{font-weight:400;display:block}
.plain-card{position:absolute;background:#fff;border:1px solid var(--line);border-radius:6px;display:flex;flex-direction:column;align-items:center;justify-content:center;text-align:center;color:var(--navy);font-weight:700;line-height:1.15;box-shadow:0 2px 6px rgba(10,40,90,.08)}
.plain-card svg{stroke:var(--navy);fill:none;stroke-width:1.6;stroke-linejoin:round;stroke-linecap:round}
.spam-title{color:var(--green);font-weight:500;letter-spacing:.3px}
.partners{display:flex;flex-wrap:wrap;align-content:center;justify-content:space-around;gap:4px 10px;font-family:"Work Sans",Arial,sans-serif;font-weight:600;color:#6b7280}
.feature{position:absolute;display:grid;grid-template-columns:30px 1fr}
.feature svg{stroke:var(--accent);fill:none;stroke-width:1.6;stroke-linecap:round;stroke-linejoin:round}
.feature h4{font-size:9.5px;color:var(--navy);font-weight:700;margin-bottom:3px}
.feature p{font-size:9px;line-height:1.5;color:var(--muted)}
.phone{position:absolute;background:var(--pale);border:2px solid #D5DFEA;border-bottom:none;border-radius:22px 22px 0 0;overflow:hidden}
.phone-title{font-size:9.5px;color:var(--navy);font-weight:500}
.phone-note{font-size:6px;color:#8a95a8;text-align:center;background:#fff;border-radius:8px;padding:2px 0}
.quote{position:absolute;background:#fff;border-radius:4px;box-shadow:0 1px 4px rgba(0,0,0,.06)}
.quote .name{font-size:8px;font-weight:700;color:var(--ink)}
.quote .tag{display:inline-block;background:var(--check);color:#fff;font-size:5px;padding:1px 4px;border-radius:2px}
.quote .pay{font-size:5.5px;color:#8a95a8;text-align:center}
.range{position:relative;height:3px;border-radius:2px;background:linear-gradient(90deg,#3DBF4A 0 45%,#F0A030 45% 70%,#E4483B 70%)}
.range i{position:absolute;top:-3px;width:8px;height:8px;border-radius:50%;background:#fff;border:1.5px solid var(--check)}
.range-labels{display:flex;justify-content:space-between;font-size:5px;color:#8a95a8}
.q-btns{display:flex;gap:8px}
.q-btns span{flex:1;height:14px;font-size:6px;display:flex;align-items:center;justify-content:center;border-radius:2px}
.q-btns .go{background:var(--accent);color:#fff}
.q-btns .call{border:1px solid var(--accent);color:var(--accent)}
.more{font-size:5px;color:#8a95a8}
.dot{position:absolute;border-radius:50%;background:var(--pale);border:1px solid var(--ice)}
.step{position:absolute;display:grid;grid-template-columns:22px 1fr}
.step svg{stroke:var(--accent);fill:none;stroke-width:1.6}
.step h4{font-size:9.5px;color:var(--navy);font-weight:700;margin-bottom:3px}
.step p{font-size:9px;line-height:1.5;color:var(--muted)}
.step-m{position:absolute;left:10px;width:212px;text-align:center}
.step-m svg{stroke:var(--accent);fill:none;stroke-width:1.6}
.step-m h4{font-size:8px;color:var(--navy);font-weight:700;margin:3px 0 2px}
.step-m p{font-size:7px;line-height:1.45;color:var(--muted)}
.center{text-align:center}
.link{text-decoration:underline;color:var(--navy)}
.app{position:absolute;background:#fff;border:2px solid #D5DFEA;border-radius:10px 10px 0 0;overflow:hidden}
.copy-light{color:#fff}
.compare{position:absolute;font-size:8.5px;color:var(--muted)}
.compare .row{display:grid;align-items:center;border-bottom:1px solid var(--line)}
.compare .qm{background:var(--pale);height:100%;display:flex;align-items:center;justify-content:center}
.compare .other{display:flex;align-items:center;justify-content:center;height:100%}
.compare .head{font-weight:700;color:var(--navy);text-align:center;line-height:1.2}
.compare .head.qm{color:var(--accent)}
.tick{stroke:var(--check);fill:none;stroke-width:1.8;stroke-linecap:round;stroke-linejoin:round}
.dash{width:7px;height:1px;background:#6b7280}
.faq-item{position:absolute;background:var(--soft);display:flex;align-items:center;gap:8px;font-weight:600;color:var(--navy);border-radius:2px}
.faq-item b{font-weight:400;font-size:13px;color:var(--navy)}
.footer-col h5{font-size:9px;color:#fff;font-weight:700;margin-bottom:4px}
.footer-col li{list-style:none;font-size:8.5px;color:#D7E2F1;line-height:1.55}
.footer-col p{font-size:8.5px;color:#D7E2F1;line-height:1.55}
.badge{position:absolute;border-radius:50%;background:radial-gradient(circle,#ECEEF1 0 48%,#B9BEC7 50% 56%,#F2F3F5 58%);}
.legal{position:absolute;font-size:6.5px;color:#C9D6EA}
.legal u{color:#fff}
.acc{position:absolute;left:10px;width:212px;display:flex;justify-content:space-between;align-items:center;font-size:7.5px;color:#fff;font-weight:500;padding-bottom:6px;border-bottom:1px solid rgba(255,255,255,.35)}
.acc svg{stroke:#fff;fill:none;stroke-width:1.5}
.contour{background-image:repeating-radial-gradient(circle at 70% 30%,rgba(255,255,255,.025) 0 1px,transparent 1px 22px)}
</style>
</head>
<body>

<svg width="0" height="0" style="position:absolute" aria-hidden="true">
  <symbol id="ic-home" viewBox="0 0 32 32"><path d="M5 15 16 5l11 10"/><path d="M8 13v14h16V13"/><path d="M13 27v-8h6v8"/></symbol>
  <symbol id="ic-car" viewBox="0 0 32 32"><path d="M6 20v-4l3-7h14l3 7v4"/><path d="M5 16h22v6H5z"/><circle cx="10" cy="24" r="2.5"/><circle cx="22" cy="24" r="2.5"/><path d="M10 13h12"/></symbol>
  <symbol id="ic-bundle" viewBox="0 0 32 32"><path d="M8 14 18 5l11 9"/><path d="M11 12v4M27 12v14h-5"/><path d="M3 22v-3l2-5h10l2 5v3"/><path d="M2 19h16v5H2z"/><circle cx="6" cy="26" r="2"/><circle cx="14" cy="26" r="2"/></symbol>
  <symbol id="ic-check-circle" viewBox="0 0 24 24"><circle cx="12" cy="12" r="9"/><path d="m8 12 3 3 5-6"/></symbol>
  <symbol id="ic-trophy" viewBox="0 0 24 24"><path d="M7 4h10v5a5 5 0 0 1-10 0z"/><path d="M7 6H4v2a3 3 0 0 0 3 3M17 6h3v2a3 3 0 0 1-3 3"/><path d="M12 14v4M8 20h8"/></symbol>
  <symbol id="ic-bell-off" viewBox="0 0 24 24"><path d="M6 17h12l-2-3V10a4 4 0 0 0-7-2.6"/><path d="M6 10v4l-2 3"/><path d="M10 20h4"/><path d="M3 3l18 18"/></symbol>
  <symbol id="ic-chat" viewBox="0 0 24 24"><path d="M4 12a8 8 0 1 1 3 6l-4 1 1-4a8 8 0 0 1 0-3z"/><circle cx="9" cy="12" r=".6"/><circle cx="12" cy="12" r=".6"/><circle cx="15" cy="12" r=".6"/></symbol>
  <symbol id="ic-list" viewBox="0 0 24 24"><rect x="4" y="4" width="16" height="6" rx="1"/><rect x="4" y="14" width="16" height="6" rx="1"/></symbol>
  <symbol id="ic-dollar" viewBox="0 0 24 24"><circle cx="12" cy="12" r="9"/><path d="M15 9c-1-1.5-6-1.5-6 .8 0 2.7 6 1.4 6 4.2 0 2.3-5 2.3-6 .8M12 6v12"/></symbol>
  <symbol id="ic-tick" viewBox="0 0 12 12"><path d="m2 6 3 3 5-6"/></symbol>
  <symbol id="ic-chev" viewBox="0 0 12 12"><path d="m3 4.5 3 3 3-3"/></symbol>
</svg>

<!-- ================= DESKTOP ================= -->
<div class="device desktop">

  <header class="band white" style="top:0;height:64px">
    <div class="brand abs" style="left:66px;top:21px;font-size:18px"><span class="brand-mark" style="width:16px;height:16px"></span>QuoteMarlin</div>
    <nav class="nav abs" style="left:462px;top:26px"><span>Car Insurance</span><span>Life Insurance</span><span>Resources</span><span>Company</span></nav>
    <a class="btn btn-solid abs" style="left:762px;top:19px;width:84px;height:27px">Compare Now</a>
  </header>

  <section class="band navy contour" style="top:64px;height:376px">
    <div class="abs photo" role="img" aria-label="Golden retriever wearing a yellow bandana" style="left:22px;top:112px;width:248px;height:264px"></div>
    <h1 class="abs copy-light" style="left:318px;top:84px;font-size:30px;font-weight:600">Compare insurance rates</h1>
    <p class="abs copy-light" style="left:318px;top:118px;font-size:15px">See what you should pay at top companies near you</p>
    <a class="type-card" style="left:318px;top:150px;width:112px;height:110px;font-size:11.5px"><svg width="36" height="36"><use href="#ic-home"/></svg>Home<small>insurance</small></a>
    <a class="type-card" style="left:458px;top:150px;width:112px;height:110px;font-size:11.5px"><svg width="36" height="36"><use href="#ic-car"/></svg>Car<small>insurance</small></a>
    <a class="type-card" style="left:598px;top:150px;width:112px;height:110px;font-size:11.5px"><svg width="36" height="36"><use href="#ic-bundle"/></svg>Bundled<small>(home + car)</small></a>
    <p class="abs spam-title" style="left:318px;top:294px;font-size:12px">SPAM FREE ZONE</p>
    <p class="abs copy-light" style="left:318px;top:312px;font-size:12px">We won't hound you with unwanted calls or emails – EVER!</p>
  </section>

  <div class="band white partners" style="top:440px;height:56px;font-size:11px;padding:0 12px">
    <span>Fennick</span><span>Halvory</span><span>Brundell</span><span>Cobbery</span><span>Marlowick</span><span>Sablewick</span><span>Tarnwell</span><span>Quenby</span><span>Wrenholt</span><span>Ashvorne</span><span>Pellory</span><span>Glimmerby</span><span>Stonevarre</span>
  </div>

  <section class="band soft" style="top:496px;height:384px">
    <h2 class="abs" style="left:86px;top:56px;font-size:23px;line-height:1.25;color:var(--navy)">Everything you need to make the<br><span class="hl">right decisions</span></h2>
    <div class="feature" style="left:86px;top:148px;width:460px"><svg width="20" height="20"><use href="#ic-check-circle"/></svg><div><h4>No bait and switch – accurate rate estimates using better data</h4><p>No low-ball quotes. We use the rating plans submitted by each insurance carrier to the state department of insurance plus any applicable discounts to more accurately calculate what you can expect to pay.</p></div></div>
    <div class="feature" style="left:86px;top:226px;width:460px"><svg width="20" height="20"><use href="#ic-trophy"/></svg><div><h4>More choices – not limited to paid advertisers</h4><p>Unlike other sites, our results are not limited to paid sponsors. Our results represent top carriers in your geographic area based on the total premiums written.</p></div></div>
    <div class="feature" style="left:86px;top:288px;width:460px"><svg width="20" height="20"><use href="#ic-bell-off"/></svg><div><h4>Spam-free – no contact information required</h4><p>We are the only insurance comparison tool that does not require your contact information to generate your estimates, so you can be sure you won't get spam from us.</p></div></div>

    <div class="phone" style="left:590px;top:56px;width:216px;height:328px">
      <p class="abs phone-title" style="left:16px;top:46px">Our recommendations</p>
      <p class="abs phone-note" style="left:40px;top:72px;width:136px">How we order results</p>
      <div class="quote" style="left:16px;top:100px;width:184px;height:110px;padding:8px 10px 0 30px">
        <span class="dot" style="left:8px;top:20px;width:16px;height:16px"></span>
        <p class="name">Quillmere Mutual</p><span class="tag">Best match</span>
        <p class="pay" style="margin:4px 0">Expect to pay around $1000</p>
        <div class="range"><i style="left:30%"></i></div>
        <div class="range-labels" style="margin:3px 0 6px"><span>Below</span><span>Average</span><span>Above</span></div>
        <div class="q-btns"><span class="go">Get quote</span><span class="call">Call now</span></div>
        <p class="more" style="margin-top:4px">+ View details</p>
      </div>
      <div class="quote" style="left:16px;top:222px;width:184px;height:110px;padding:8px 10px 0 30px">
        <span class="dot" style="left:8px;top:20px;width:16px;height:16px"></span>
        <p class="name">Dovecrest</p>
        <p class="pay" style="margin:4px 0">Expect to pay around $1000</p>
        <div class="range"><i style="left:34%"></i></div>
        <div class="range-labels" style="margin:3px 0 6px"><span>Below</span><span>Average</span><span>Above</span></div>
        <div class="q-btns"><span class="go">Get quote</span><span class="call">Call now</span></div>
      </div>
    </div>
  </section>

  <section class="band white" style="top:880px;height:424px">
    <h2 class="abs center" style="left:0;right:0;top:66px;font-size:23px;line-height:1.3;color:var(--ink)">Insurance shopping can be pleasant - like a<br>relaxing scroll through the <span class="hl">best rates</span></h2>
    <p class="abs center" style="left:0;right:0;top:130px;font-size:13px;font-weight:700;color:var(--navy)">Start saving in <span class="hl">3 simple steps</span></p>
    <div class="step" style="left:158px;top:186px;width:190px"><svg width="18" height="18"><use href="#ic-chat"/></svg><div><h4>Quick start</h4><p>Answer 5 questions. No phone number or email required.</p></div></div>
    <div class="step" style="left:362px;top:186px;width:190px"><svg width="18" height="18"><use href="#ic-list"/></svg><div><h4>Retrieve your rates</h4><p>We estimate how much you'll pay at each top provider in your state.</p></div></div>
    <div class="step" style="left:563px;top:186px;width:190px"><svg width="18" height="18"><use href="#ic-dollar"/></svg><div><h4>Compare and save</h4><p>Compare apples to apples pricing to find your next provider.</p></div></div>
    <a class="btn btn-solid abs" style="left:386px;top:269px;width:124px;height:30px;font-size:10px">Get Started</a>
    <p class="abs center" style="left:0;right:0;top:315px;font-size:9px">Read our <span class="link">spam-free promise</span></p>
  </section>

  <section class="band navy contour" style="top:1304px;height:371px">
    <h2 class="abs copy-light" style="left:477px;top:56px;font-size:23px;line-height:1.3">Lifting the curtain <span class="hl-green">on the<br>insurance industry</span></h2>
    <p class="abs copy-light" style="left:477px;top:142px;width:330px;font-size:9px;line-height:1.6">Insurance companies have rating plans that detail how they use certain characteristics to assign different rates to different people. These rating plans must be approved by your state department of insurance but are not typically available to consumers.</p>
    <p class="abs copy-light" style="left:477px;top:208px;width:330px;font-size:9px;line-height:1.6">QuoteMarlin uses the data from each insurance company's rating plan (plus any applicable discounts) to more accurately calculate what you can expect to pay.</p>
    <a class="btn btn-dash abs" style="left:477px;top:299px;width:101px;height:27px">Start Comparing</a>
  </section>
  <div class="app" style="left:59px;top:1261px;width:347px;height:414px">
    <div class="brand abs" style="left:10px;top:12px;font-size:7px"><span class="brand-mark" style="width:6px;height:6px"></span>QuoteMarlin</div>
    <div class="abs" style="left:10px;top:40px;width:42px;height:12px;border:1px solid var(--line);border-radius:6px;font-size:5px;display:flex;align-items:center;justify-content:center">← Go Back</div>
    <div class="abs" style="left:0;top:60px;width:100px;bottom:0;background:#F6F8FB"></div>
    <p class="abs" style="left:12px;top:80px;width:78px;font-size:5px;line-height:1.5;color:#8a95a8">Adjust filters to refine your results list below</p>
    <p class="abs" style="left:20px;top:100px;font-size:5px;line-height:2.2;color:#8a95a8">Driver details<br>Vehicle details<br>Coverage level</p>
    <div class="abs btn btn-solid" style="left:14px;top:136px;width:72px;height:9px;font-size:5px">Recalculate</div>
    <p class="abs center" style="left:110px;width:230px;top:40px;font-size:6.5px;font-weight:700">Range of Annual Rates</p>
    <p class="abs center" style="left:110px;width:230px;top:50px;font-size:5px;color:#8a95a8">Based on your information from companies in your area</p>
    <div class="abs" style="left:126px;top:78px;width:200px;height:2px;background:var(--accent)"></div>
    <span class="abs" style="left:122px;top:75px;width:7px;height:7px;border-radius:50%;background:#fff;border:1.5px solid var(--check)"></span>
    <span class="abs" style="left:206px;top:75px;width:7px;height:7px;border-radius:50%;background:#fff;border:1.5px solid var(--check)"></span>
    <span class="abs" style="left:322px;top:75px;width:7px;height:7px;border-radius:50%;background:#fff;border:1.5px solid var(--accent)"></span>
    <p class="abs" style="left:130px;top:132px;font-size:6px;font-weight:700">Your Results</p>
    <p class="abs" style="left:130px;top:142px;font-size:4.5px;color:#8a95a8">Sorted by best match for your profile</p>
    <div class="quote" style="left:126px;top:160px;width:210px;height:66px;padding:6px 8px"><p class="name" style="font-size:6.5px">Quillmere Mutual</p><span class="tag">Best match</span><p class="pay">Expect to pay around $1000</p><div class="range" style="margin-top:8px;width:130px"><i style="left:30%"></i></div><span class="abs btn btn-solid" style="right:8px;top:6px;width:50px;height:9px;font-size:4.5px">Get quote</span><span class="abs" style="right:8px;top:18px;width:50px;height:9px;border:1px solid var(--accent);font-size:4.5px;color:var(--accent);display:flex;align-items:center;justify-content:center">Call now</span></div>
    <div class="quote" style="left:126px;top:254px;width:210px;height:66px;padding:6px 8px"><p class="name" style="font-size:6.5px">Thistlebay</p><span class="tag">Good value</span><p class="pay">Expect to pay around $1000</p><div class="range" style="margin-top:8px;width:130px"><i style="left:40%"></i></div><span class="abs btn btn-solid" style="right:8px;top:6px;width:50px;height:9px;font-size:4.5px">Online quote</span><span class="abs" style="right:8px;top:18px;width:50px;height:9px;border:1px solid var(--accent);font-size:4.5px;color:var(--accent);display:flex;align-items:center;justify-content:center">Talk to an agent</span></div>
    <div class="quote" style="left:126px;top:344px;width:210px;height:66px;padding:6px 8px"><p class="name" style="font-size:6.5px">Marrowgate</p><span class="tag">Low price</span><p class="pay">Expect to pay around $1000</p><div class="range" style="margin-top:8px;width:130px"><i style="left:36%"></i></div><span class="abs btn btn-solid" style="right:8px;top:6px;width:50px;height:9px;font-size:4.5px">Get quote</span><span class="abs" style="right:8px;top:18px;width:50px;height:9px;border:1px solid var(--accent);font-size:4.5px;color:var(--accent);display:flex;align-items:center;justify-content:center">Call now</span></div>
  </div>

  <section class="band white" style="top:1675px;height:565px">
    <h2 class="abs center" style="left:0;right:0;top:56px;font-size:23px;line-height:1.3;color:var(--ink)">Your free and impartial insurance<br><span class="hl">research tool</span></h2>
    <p class="abs center" style="left:150px;right:150px;top:126px;font-size:9px;line-height:1.6;color:var(--muted)">We're passionate about giving you open access to the data you need to make smart insurance decisions. We don't sell insurance policies directly – our tool allows you independently research your options and seamlessly connect with the provider that works for you.</p>
    <div class="compare" style="left:109px;top:186px;width:474px">
      <div class="row" style="grid-template-columns:274px 104px 96px;height:38px;border:none"><span></span><span class="head qm">QuoteMarlin</span><span class="head">Other comparison<br>sites</span></div>
      <div class="row" style="grid-template-columns:274px 104px 96px;height:38px"><span style="padding-left:10px">Connects you with the provider you choose</span><span class="qm"><svg width="12" height="12" class="tick"><use href="#ic-tick"/></svg></span><span class="other"><svg width="12" height="12" class="tick"><use href="#ic-tick"/></svg></span></div>
      <div class="row" style="grid-template-columns:274px 104px 96px;height:38px"><span style="padding-left:10px">No email or phone number required</span><span class="qm"><svg width="12" height="12" class="tick"><use href="#ic-tick"/></svg></span><span class="other"><i class="dash"></i></span></div>
      <div class="row" style="grid-template-columns:274px 104px 96px;height:38px"><span style="padding-left:10px">Rates for all top companies in your state</span><span class="qm"><svg width="12" height="12" class="tick"><use href="#ic-tick"/></svg></span><span class="other"><i class="dash"></i></span></div>
      <div class="row" style="grid-template-columns:274px 104px 96px;height:38px"><span style="padding-left:10px">Accurate rates verified with state-approved rating plans</span><span class="qm"><svg width="12" height="12" class="tick"><use href="#ic-tick"/></svg></span><span class="other"><i class="dash"></i></span></div>
      <div class="row" style="grid-template-columns:274px 104px 96px;height:38px"><span style="padding-left:10px">Results not limited to companies with paid sponsorships</span><span class="qm"><svg width="12" height="12" class="tick"><use href="#ic-tick"/></svg></span><span class="other"><i class="dash"></i></span></div>
      <div class="row" style="grid-template-columns:274px 104px 96px;height:38px"><span style="padding-left:10px">Results shown after just 5 questions</span><span class="qm"><svg width="12" height="12" class="tick"><use href="#ic-tick"/></svg></span><span class="other"><i class="dash"></i></span></div>
      <div class="row" style="grid-template-columns:274px 104px 96px;height:38px"><span style="padding-left:10px">Option to purchase a policy through them</span><span class="qm"><svg width="12" height="12" class="tick"><use href="#ic-tick"/></svg></span><span class="other"><svg width="12" height="12" class="tick"><use href="#ic-tick"/></svg></span></div>
    </div>
    <div class="abs photo" role="img" aria-label="Golden retriever sitting, wearing a yellow bandana" style="left:606px;top:189px;width:160px;height:296px"></div>
  </section>

  <section class="band white" style="top:2240px;height:464px">
    <h2 class="abs center" style="left:0;right:0;top:29px;font-size:23px;color:var(--ink)">Frequently asked <span class="hl">questions</span></h2>
    <div class="faq-item" style="left:109px;width:676px;top:69px;height:36px;padding-left:12px;font-size:9.5px"><b>+</b>How does the insurance company determine my rate?</div>
    <div class="faq-item" style="left:109px;width:676px;top:111px;height:36px;padding-left:12px;font-size:9.5px"><b>+</b>How do I switch my car insurance?</div>
    <div class="faq-item" style="left:109px;width:676px;top:153px;height:36px;padding-left:12px;font-size:9.5px"><b>+</b>How is QuoteMarlin different than other insurance websites?</div>
    <div class="faq-item" style="left:109px;width:676px;top:195px;height:36px;padding-left:12px;font-size:9.5px"><b>+</b>How does QuoteMarlin make money?</div>
    <div class="faq-item" style="left:109px;width:676px;top:237px;height:36px;padding-left:12px;font-size:9.5px"><b>+</b>You say you don't limit results – why do I only see up to 12?</div>
    <div class="faq-item" style="left:109px;width:676px;top:279px;height:36px;padding-left:12px;font-size:9.5px"><b>+</b>How can I get cheaper car insurance?</div>
    <div class="faq-item" style="left:109px;width:676px;top:321px;height:36px;padding-left:12px;font-size:9.5px"><b>+</b>How much car insurance do I need?</div>
    <a class="btn btn-solid abs" style="left:337px;top:384px;width:96px;height:28px">Open FAQ Page</a>
    <a class="btn btn-dash abs" style="left:461px;top:384px;width:98px;height:28px">Contact Us</a>
  </section>

  <section class="band soft" style="top:2704px;height:283px">
    <div class="abs photo" role="img" aria-label="Golden retriever lying down, wearing a yellow bandana" style="left:214px;top:43px;width:184px;height:184px"></div>
    <h2 class="abs" style="left:424px;top:71px;font-size:23px;color:var(--ink)">Ready, set, <span class="hl">retrieve</span></h2>
    <p class="abs" style="left:424px;top:104px;width:280px;font-size:9.5px;font-weight:700;line-height:1.4;color:var(--navy)">Ready to get started? Dig up the <span class="hl">best insurance</span> providers in seconds</p>
    <a class="plain-card" style="left:427px;top:144px;width:82px;height:83px;font-size:9px"><svg width="28" height="28"><use href="#ic-home"/></svg>Home<small style="font-weight:400">insurance</small></a>
    <a class="plain-card" style="left:533px;top:144px;width:82px;height:83px;font-size:9px"><svg width="28" height="28"><use href="#ic-car"/></svg>Car<small style="font-weight:400">insurance</small></a>
    <a class="plain-card" style="left:640px;top:144px;width:82px;height:83px;font-size:9px"><svg width="28" height="28"><use href="#ic-bundle"/></svg>Bundled<small style="font-weight:400">(home + car)</small></a>
  </section>

  <footer class="band navy" style="top:2987px;height:210px">
    <div class="footer-col abs" style="left:86px;top:29px;width:180px"><h5>About QuoteMarlin</h5><p>QuoteMarlin is your insurance companion – connecting you with top auto insurance providers without collecting your contact information.</p></div>
    <div class="footer-col abs" style="left:301px;top:29px"><h5>Resources</h5><ul><li>Insurance by state</li><li>FAQ</li><li>Insurance by age</li><li>Show All</li></ul></div>
    <div class="footer-col abs" style="left:430px;top:29px"><h5>Company</h5><ul><li>Contact us</li><li>How we make money</li><li>Spam-free promise</li><li>Partner with us</li></ul></div>
    <div class="footer-col abs" style="left:573px;top:29px"><h5>Support</h5><ul><li>Editorial policy</li><li>Accessibility statement</li><li>Cookie policy</li><li>California Residents:<br>Do not sell my info</li></ul></div>
    <div class="badge" role="img" aria-label="Growth award badge" style="left:726px;top:21px;width:80px;height:80px"></div>
    <p class="abs" style="left:86px;top:148px;font-size:9px;font-weight:700;color:#fff">Find coverage in your state</p>
    <p class="legal" style="left:86px;top:183px">Copyright © QuoteMarlin Insurance Services 2023. A Velloran Company. All Rights Reserved Use of QuoteMarlin's services is subject to our <u>Privacy Policy</u>, <u>Disclaimer</u>, and <u>Terms and Conditions</u>.</p>
  </footer>
</div>

<!-- ================= MOBILE ================= -->
<div class="device mobile">
  <header class="band white" style="top:0;height:32px">
    <div class="brand abs" style="left:10px;top:9px;font-size:11px"><span class="brand-mark" style="width:10px;height:10px"></span>QuoteMarlin</div>
    <svg class="abs" style="right:12px;top:10px" width="12" height="10" stroke="#0F1A33" stroke-width="1.4"><path d="M0 1h12M0 5h12M0 9h12"/></svg>
  </header>

  <section class="band navy contour" style="top:32px;height:384px">
    <h1 class="abs center copy-light" style="left:0;right:0;top:22px;font-size:15px;font-weight:600">Compare insurance rates</h1>
    <p class="abs center copy-light" style="left:20px;right:20px;top:43px;font-size:8px;line-height:1.3">See what you should pay at top companies near you</p>
    <a class="type-card" style="left:10px;top:85px;width:67px;height:62px;font-size:6.5px"><svg width="20" height="20"><use href="#ic-home"/></svg>Home<small>insurance</small></a>
    <a class="type-card" style="left:83px;top:85px;width:67px;height:62px;font-size:6.5px"><svg width="20" height="20"><use href="#ic-car"/></svg>Car<small>insurance</small></a>
    <a class="type-card" style="left:157px;top:85px;width:67px;height:62px;font-size:6.5px"><svg width="20" height="20"><use href="#ic-bundle"/></svg>Bundled<small>(home + car)</small></a>
    <p class="abs center spam-title" style="left:0;right:0;top:174px;font-size:8.5px">SPAM FREE ZONE</p>
    <p class="abs center copy-light" style="left:10px;right:10px;top:190px;font-size:8px;line-height:1.35">We won't hound you with unwanted calls or emails - EVER!</p>
    <div class="abs photo" role="img" aria-label="Golden retriever wearing a yellow bandana" style="left:3px;top:224px;width:109px;height:160px"></div>
    <div class="abs partners" style="left:112px;top:350px;width:120px;height:34px;background:#fff;font-size:6.5px;gap:2px 6px">
      <span>Hedgeroam</span><span>Tamsin Mutual</span><span>Halvory</span>
    </div>
  </section>

  <section class="band soft" style="top:416px;height:856px">
    <h2 class="abs center" style="left:10px;right:10px;top:30px;font-size:14px;line-height:1.3;color:var(--navy)">Everything you need to make the <span class="hl">right decisions</span></h2>
    <div class="abs center" style="left:10px;width:212px;top:88px"><svg width="20" height="20" stroke="var(--accent)" fill="none" stroke-width="1.6"><use href="#ic-check-circle"/></svg><h4 style="font-size:8px;color:var(--navy);margin:4px 0 3px">No bait and switch – accurate rate estimates using better data</h4><p style="font-size:7px;line-height:1.45;color:var(--muted)">No low-ball quotes. We use the rating plans submitted by each insurance carrier to the state department of insurance plus any applicable discounts to more accurately calculate what you can expect to pay.</p></div>
    <div class="abs center" style="left:10px;width:212px;top:230px"><svg width="20" height="20" stroke="var(--accent)" fill="none" stroke-width="1.6"><use href="#ic-trophy"/></svg><h4 style="font-size:8px;color:var(--navy);margin:4px 0 3px">More choices – not limited to paid advertisers</h4><p style="font-size:7px;line-height:1.45;color:var(--muted)">Unlike other sites, our results are not limited to paid sponsors. Our results represent top carriers in your geographic area based on the total premiums written.</p></div>
    <div class="abs center" style="left:10px;width:212px;top:363px"><svg width="20" height="20" stroke="var(--accent)" fill="none" stroke-width="1.6"><use href="#ic-bell-off"/></svg><h4 style="font-size:8px;color:var(--navy);margin:4px 0 3px">Spam-free – no contact information required</h4><p style="font-size:7px;line-height:1.45;color:var(--muted)">We are the only insurance comparison tool that does not require your contact information to generate your estimates, so you can be sure you won't get spam from us.</p></div>
    <div class="phone" style="left:10px;top:496px;width:213px;height:360px">
      <p class="abs phone-title" style="left:16px;top:46px">Our recommendations</p>
      <p class="abs phone-note" style="left:40px;top:70px;width:133px">How we order results</p>
      <div class="quote" style="left:16px;top:100px;width:182px;height:118px;padding:8px 10px 0 30px">
        <span class="dot" style="left:8px;top:24px;width:16px;height:16px"></span>
        <p class="name">Quillmere Mutual</p><span class="tag">Best match</span>
        <p class="pay" style="margin:4px 0">Expect to pay around $1000</p>
        <div class="range"><i style="left:30%"></i></div>
        <div class="range-labels" style="margin:3px 0 6px"><span>Below</span><span>Average</span><span>Above</span></div>
        <div class="q-btns"><span class="go">Get quote</span><span class="call">Call now</span></div>
        <p class="more" style="margin-top:4px">+ View details</p>
      </div>
      <div class="quote" style="left:16px;top:230px;width:182px;height:118px;padding:8px 10px 0 30px">
        <span class="dot" style="left:8px;top:24px;width:16px;height:16px"></span>
        <p class="name">Dovecrest</p>
        <p class="pay" style="margin:4px 0">Expect to pay around $1000</p>
        <div class="range"><i style="left:34%"></i></div>
        <div class="range-labels" style="margin:3px 0 6px"><span>Below</span><span>Average</span><span>Above</span></div>
        <div class="q-btns"><span class="go">Get quote</span><span class="call">Call now</span></div>
        <p class="more" style="margin-top:4px">+ View details</p>
      </div>
    </div>
  </section>

  <section class="band white" style="top:1272px;height:504px">
    <h2 class="abs center" style="left:8px;right:8px;top:34px;font-size:14px;line-height:1.3;color:var(--ink)">Insurance shopping can be pleasant - like a relaxing scroll through the <span class="hl">best rates</span></h2>
    <p class="abs center" style="left:0;right:0;top:118px;font-size:8.5px;font-weight:700;color:var(--navy)">Start saving in <span class="hl">3 simple steps</span></p>
    <div class="step-m" style="top:148px"><svg width="16" height="16"><use href="#ic-chat"/></svg><h4>Quick start</h4><p>Answer 5 questions. No phone number or email required.</p></div>
    <div class="step-m" style="top:242px"><svg width="16" height="16"><use href="#ic-list"/></svg><h4>Retrieve your rates</h4><p>We estimate how much you'll pay at each top provider in your state.</p></div>
    <div class="step-m" style="top:336px"><svg width="16" height="16"><use href="#ic-dollar"/></svg><h4>Compare and save</h4><p>Compare apples to apples pricing to find your next provider.</p></div>
    <a class="btn btn-solid abs" style="left:10px;top:418px;width:213px;height:29px;font-size:9px">Get Started</a>
    <p class="abs center" style="left:0;right:0;top:462px;font-size:7.5px">Read our <span class="link">spam-free promise</span></p>
  </section>

  <section class="band navy contour" style="top:1776px;height:547px">
    <h2 class="abs center copy-light" style="left:8px;right:8px;top:30px;font-size:14px;line-height:1.3">Lifting the curtain <span class="hl-green">on the insurance industry</span></h2>
    <div class="app" style="left:10px;top:80px;width:202px;height:259px;border-radius:8px">
      <div class="brand abs" style="left:8px;top:8px;font-size:5px"><span class="brand-mark" style="width:4px;height:4px"></span>QuoteMarlin</div>
      <div class="abs" style="left:0;top:30px;width:56px;bottom:0;background:#F6F8FB"></div>
      <p class="abs center" style="left:62px;width:134px;top:28px;font-size:4.5px;font-weight:700">Range of Annual Rates</p>
      <div class="abs" style="left:70px;top:50px;width:120px;height:1.5px;background:var(--accent)"></div>
      <div class="quote" style="left:68px;top:110px;width:126px;height:40px;padding:4px"><p class="name" style="font-size:4.5px">Quillmere Mutual</p><div class="range" style="margin-top:12px;height:2px"></div></div>
      <div class="quote" style="left:68px;top:162px;width:126px;height:40px;padding:4px"><p class="name" style="font-size:4.5px">Thistlebay</p><div class="range" style="margin-top:12px;height:2px"></div></div>
      <div class="quote" style="left:68px;top:212px;width:126px;height:40px;padding:4px"><p class="name" style="font-size:4.5px">Marrowgate</p><div class="range" style="margin-top:12px;height:2px"></div></div>
    </div>
    <p class="abs copy-light" style="left:10px;width:212px;top:365px;font-size:7px;line-height:1.5">Insurance companies have rating plans that detail how they use certain characteristics to assign different rates to different people. These rating plans must be approved by your state department of insurance but are not typically available to consumers.<br>QuoteMarlin uses the data from each insurance company's rating plan (plus any applicable discounts) to more accurately calculate what you can expect to pay.</p>
    <a class="btn btn-dash abs" style="left:10px;top:496px;width:213px;height:29px;font-size:8px">Start Comparing</a>
  </section>

  <section class="band white" style="top:2323px;height:573px">
    <h2 class="abs" style="left:10px;right:10px;top:48px;font-size:13px;line-height:1.3;color:var(--ink)">Your free and impartial insurance <span class="hl">research tool</span></h2>
    <p class="abs" style="left:10px;width:206px;top:92px;font-size:7px;line-height:1.5;color:var(--muted)">We're passionate about giving you open access to the data you need to make smart insurance decisions. We don't sell insurance policies directly – our tool allows you independently research your options and seamlessly connect with the provider that works for you.</p>
    <div class="compare" style="left:10px;top:189px;width:213px;font-size:6.8px">
      <div class="row" style="grid-template-columns:98px 54px 61px;height:36px;border:none"><span></span><span class="head qm" style="font-size:7px">Quote<br>Marlin</span><span class="head" style="font-size:7px">Other<br>comparison<br>sites</span></div>
      <div class="row" style="grid-template-columns:98px 54px 61px;height:44px"><span style="padding-left:6px">Connects you with the provider you choose</span><span class="qm"><svg width="10" height="10" class="tick"><use href="#ic-tick"/></svg></span><span class="other"><svg width="10" height="10" class="tick"><use href="#ic-tick"/></svg></span></div>
      <div class="row" style="grid-template-columns:98px 54px 61px;height:40px"><span style="padding-left:6px">No email or phone number required</span><span class="qm"><svg width="10" height="10" class="tick"><use href="#ic-tick"/></svg></span><span class="other"><i class="dash"></i></span></div>
      <div class="row" style="grid-template-columns:98px 54px 61px;height:44px"><span style="padding-left:6px">Rates for all top companies in your state</span><span class="qm"><svg width="10" height="10" class="tick"><use href="#ic-tick"/></svg></span><span class="other"><i class="dash"></i></span></div>
      <div class="row" style="grid-template-columns:98px 54px 61px;height:56px"><span style="padding-left:6px">Accurate rates verified with state-approved rating plans</span><span class="qm"><svg width="10" height="10" class="tick"><use href="#ic-tick"/></svg></span><span class="other"><i class="dash"></i></span></div>
      <div class="row" style="grid-template-columns:98px 54px 61px;height:48px"><span style="padding-left:6px">Results not limited to companies with paid sponsorships</span><span class="qm"><svg width="10" height="10" class="tick"><use href="#ic-tick"/></svg></span><span class="other"><i class="dash"></i></span></div>
      <div class="row" style="grid-template-columns:98px 54px 61px;height:38px"><span style="padding-left:6px">Results shown after just 5 questions</span><span class="qm"><svg width="10" height="10" class="tick"><use href="#ic-tick"/></svg></span><span class="other"><i class="dash"></i></span></div>
      <div class="row" style="grid-template-columns:98px 54px 61px;height:40px;border:none"><span style="padding-left:6px">Option to purchase a policy through them</span><span class="qm"><svg width="10" height="10" class="tick"><use href="#ic-tick"/></svg></span><span class="other"><svg width="10" height="10" class="tick"><use href="#ic-tick"/></svg></span></div>
    </div>
  </section>

  <section class="band white" style="top:2896px;height:448px">
    <h2 class="abs" style="left:10px;top:28px;font-size:13px;color:var(--ink)">Frequently asked <span class="hl">questions</span></h2>
    <div class="faq-item" style="left:10px;width:213px;top:56px;height:42px;padding:0 10px;font-size:7px;line-height:1.4"><b>+</b>How does the insurance company determine my rate?</div>
    <div class="faq-item" style="left:10px;width:213px;top:104px;height:32px;padding:0 10px;font-size:7px"><b>+</b>How do I switch my car insurance?</div>
    <div class="faq-item" style="left:10px;width:213px;top:142px;height:42px;padding:0 10px;font-size:7px;line-height:1.4"><b>+</b>How is QuoteMarlin different than other insurance websites?</div>
    <div class="faq-item" style="left:10px;width:213px;top:190px;height:32px;padding:0 10px;font-size:7px"><b>+</b>How does QuoteMarlin make money?</div>
    <div class="faq-item" style="left:10px;width:213px;top:228px;height:42px;padding:0 10px;font-size:7px;line-height:1.4"><b>+</b>You say you don't limit results – why do I only see up to 12?</div>
    <div class="faq-item" style="left:10px;width:213px;top:276px;height:32px;padding:0 10px;font-size:7px"><b>+</b>How can I get cheaper car insurance?</div>
    <div class="faq-item" style="left:10px;width:213px;top:314px;height:32px;padding:0 10px;font-size:7px"><b>+</b>How much car insurance do I need?</div>
    <a class="btn btn-solid abs" style="left:10px;top:363px;width:98px;height:27px;font-size:8px">Open FAQ Page</a>
    <a class="btn btn-dash abs" style="left:125px;top:363px;width:98px;height:27px;font-size:8px">Contact Us</a>
  </section>

  <section class="band soft" style="top:3344px;height:304px">
    <h2 class="abs" style="left:10px;top:30px;font-size:15px;color:var(--ink)">Ready, set, <span class="hl">retrieve</span></h2>
    <p class="abs" style="left:10px;width:200px;top:55px;font-size:7.5px;font-weight:700;line-height:1.4;color:var(--navy)">Ready to get started?<br>Dig up the <span class="hl">best insurance</span> providers in seconds</p>
    <a class="plain-card" style="left:14px;top:96px;width:58px;height:52px;font-size:6.5px"><svg width="18" height="18"><use href="#ic-home"/></svg>Home<small style="font-weight:400">insurance</small></a>
    <a class="plain-card" style="left:88px;top:96px;width:58px;height:52px;font-size:6.5px"><svg width="18" height="18"><use href="#ic-car"/></svg>Car<small style="font-weight:400">insurance</small></a>
    <a class="plain-card" style="left:162px;top:96px;width:58px;height:52px;font-size:6.5px"><svg width="18" height="18"><use href="#ic-bundle"/></svg>Bundled<small style="font-weight:400">(home + car)</small></a>
    <div class="abs photo" role="img" aria-label="Golden retriever wearing a yellow bandana" style="left:56px;top:168px;width:128px;height:136px"></div>
  </section>

  <footer class="band navy" style="top:3648px;height:419px">
    <div class="footer-col abs" style="left:10px;top:20px;width:210px"><h5 style="font-size:8px">About QuoteMarlin</h5><p style="font-size:7px">QuoteMarlin is your insurance companion – connecting you with top auto insurance providers without collecting your contact information.</p></div>
    <div class="acc" style="top:92px">Resources<svg width="10" height="10"><use href="#ic-chev"/></svg></div>
    <div class="acc" style="top:125px">Company<svg width="10" height="10"><use href="#ic-chev"/></svg></div>
    <div class="acc" style="top:158px">Support<svg width="10" height="10"><use href="#ic-chev"/></svg></div>
    <div class="acc" style="top:191px">Find coverage in your state<svg width="10" height="10"><use href="#ic-chev"/></svg></div>
    <div class="badge" role="img" aria-label="Growth award badge" style="left:75px;top:240px;width:82px;height:82px"></div>
    <p class="legal center" style="left:10px;width:212px;top:344px;line-height:1.5">Copyright © QuoteMarlin Insurance Services 2023. A Velloran Company. All Rights Reserved.</p>
    <p class="legal center" style="left:10px;width:212px;top:378px;line-height:1.5">Use of QuoteMarlin's services is subject to our <u>Privacy Policy</u>, <u>Disclaimer</u>, and <u>Terms and Conditions</u>.</p>
  </footer>
</div>

</body>
</html>
```